Business Card Design

We need a design for business cards for our company. We have a logo. We teach EMT's and we are based out of Virginia. The information that will need to add would be, name, title, phone number, email, address. On the back of the business card would be "We help you, help others"

Target Market(s)

People that want to become EMT's

Colors

Designer to choose colors to be used in the design.

Requirements
Must have
• company logo

```html
<!DOCTYPE html>
<html lang="en">
<head>
<meta charset="utf-8">
<title>Medic Path Training – Business Card</title>
<link rel="stylesheet" href="https://fonts.googleapis.com/css2?family=Arimo:wght@400;700&display=swap">
<style>
  :root {
    --navy: #202a35;
    --red: #ee2c47;
    --ink: #2d2d2f;
    --paper: #ffffff;
    --paper-edge: #e3e4e6;
  }
  * { margin: 0; padding: 0; box-sizing: border-box; }
  html, body { width: 1200px; height: 686px; overflow: hidden; }
  body { font-family: "Arimo", Arial, sans-serif; background: var(--paper); }

  .card { position: relative; width: 1200px; height: 686px; overflow: hidden;
    background: radial-gradient(ellipse 60% 75% at 78% 50%, var(--paper) 45%, var(--paper-edge) 100%); }

  .brand-panel { position: absolute; left: 0; top: 0; width: 673px; height: 686px; background: var(--navy); }
  .brand { position: absolute; left: 58px; top: 322px; display: flex; align-items: center; gap: 16px; }
  .brand-dot { width: 34px; height: 34px; border-radius: 50%; background: var(--red); }
  .brand-name { color: var(--red); font-weight: 700; font-size: 48px; letter-spacing: -0.5px; white-space: nowrap; }

  .divider { position: absolute; left: 663px; top: 89px; width: 19px; height: 508px; background: var(--red); }

  .person { position: absolute; left: 757px; top: 178px; padding-left: 23px; }
  .person::before { content: ""; position: absolute; left: 0; top: 0; width: 12px; height: 86px; background: var(--red); }
  .person-name { font-size: 43px; line-height: 46px; color: var(--ink); font-weight: 400; }
  .person-name .surname { color: var(--red); }
  .person-title { font-size: 38px; line-height: 44px; color: var(--ink); margin-top: -2px; }

  .contacts { position: absolute; left: 735px; top: 301px; list-style: none; }
  .contact { display: flex; align-items: flex-start; font-size: 29px; line-height: 38px; color: var(--ink); margin-bottom: 13px; }
  .contact-icon { width: 30px; height: 30px; margin-right: 19px; margin-top: 5px; flex: none; }
  .contact-icon svg { width: 30px; height: 30px; display: block; }
</style>
</head>
<body>
<main class="card">
  <section class="brand-panel">
    <div class="brand">
      <span class="brand-dot"></span>
      <span class="brand-name">MEDIC PATH TRAINING</span>
    </div>
  </section>

  <div class="divider"></div>

  <section class="person">
    <h1 class="person-name">Daniel <span class="surname">Hart</span></h1>
    <p class="person-title">Director</p>
  </section>

  <ul class="contacts">
    <li class="contact">
      <span class="contact-icon"><svg viewBox="0 0 30 30"><rect x="9" y="3" width="14" height="24" rx="3" fill="var(--red)"/><rect x="11.5" y="6.5" width="9" height="15" fill="#fff"/><circle cx="16" cy="24" r="1.3" fill="#fff"/><path d="M3 18c0-3 2-5 6-5v11c-4 0-6-3-6-6z" fill="var(--red)"/></svg></span>
      0522 44 67890
    </li>
    <li class="contact">
      <span class="contact-icon"><svg viewBox="0 0 30 30"><rect x="2" y="8" width="26" height="16" fill="var(--red)"/><path d="M2 8l13 9 13-9" fill="none" stroke="#fff" stroke-width="2"/></svg></span>
      Info@medicpathtr.com
    </li>
    <li class="contact">
      <span class="contact-icon"><svg viewBox="0 0 30 30"><circle cx="15" cy="15" r="12" fill="var(--red)"/><rect x="2" y="12" width="26" height="6" fill="#fff"/><text x="15" y="17" font-size="6" font-family="Arial, sans-serif" font-weight="700" text-anchor="middle" fill="var(--red)">www</text></svg></span>
      www.medicpathtr.com
    </li>
    <li class="contact">
      <span class="contact-icon"><svg viewBox="0 0 30 30"><path d="M15 3a7 7 0 0 0-7 7c0 5 7 12 7 12s7-7 7-12a7 7 0 0 0-7-7z" fill="none" stroke="var(--red)" stroke-width="2"/><circle cx="15" cy="10" r="2.5" fill="var(--red)"/><path d="M4 20h5l6 6 6-6h5l2 7H2z" fill="none" stroke="var(--red)" stroke-width="1.8"/></svg></span>
      2205/46 kent street,<br>carlton vic 3053
    </li>
  </ul>
</main>
</body>
</html>
```